Maple Hollow Summer Swim Bag Tag Design

Hello!

We are looking to design a 2-sided bag tag for a children's summer swim team. Colors should be blue, white, pink. May also use a lighter blue or navy as an accent if needed. Attached are 2 files showing the look/feel of some of our other items. The bag tag would need to be in line with this same look.

Copy: Maple Hollow Otters Swim 2026
#paddlesout

The copy can be both on one side, or split between the 2 sides, either works. We are flexible! Needs to incorporate the 2026 logo into the design.

```html
<!DOCTYPE html>
<html lang="en">
<head>
<meta charset="utf-8">
<title>Maple Hollow Summer Swim Bag Tag</title>
<link href="https://fonts.googleapis.com/css2?family=Montserrat:wght@400;700;800&family=Poppins:wght@600;700&display=swap" rel="stylesheet">
<style>
  :root {
    --blue: #3a67b4;
    --blue-deep: #2d5aa8;
    --blue-light: #6f94d1;
    --pink: #ea6aa8;
    --white: #ffffff;
    --backdrop: #ebebeb;
    --slot: #ebebeb;
  }
  * { box-sizing: border-box; margin: 0; padding: 0; }
  html, body { width: 1200px; height: 1200px; overflow: hidden; background: var(--backdrop); }
  .canvas { position: relative; width: 1200px; height: 1200px; }

  .tag { position: absolute; width: 410px; height: 594px; border-radius: 26px; overflow: hidden; }
  .tag-slot { position: absolute; left: 150px; top: 45px; width: 110px; height: 34px; border-radius: 50%; background: var(--slot); }

  .edge-band { position: absolute; top: 0; bottom: 0; width: 26px; }

  /* Front */
  .tag-front { left: 133px; top: 520px; background: var(--blue); }
  .tag-front .edge-band { background: linear-gradient(180deg, #7da0d8, #5e86c8); }
  .tag-front .edge-left { left: 0; }
  .tag-front .edge-right { right: 0; }

  .year-digit { position: absolute; font-family: "Poppins", sans-serif; font-weight: 600; font-size: 205px; line-height: 1; color: var(--white); }
  .year-2a { left: 62px; top: 100px; }
  .year-2b { left: 108px; top: 262px; }
  .year-6 { left: 205px; top: 262px; color: var(--pink); }

  .year-ring { position: absolute; left: 203px; top: 112px; width: 150px; height: 150px; border-radius: 50%; border: 22px solid var(--white); background: var(--blue); display: flex; align-items: center; justify-content: center; text-align: center; }
  .ring-name { font-family: "Montserrat", sans-serif; font-weight: 700; font-size: 14px; line-height: 1.15; color: var(--white); }

  .front-hashtag { position: absolute; left: 0; right: 0; bottom: 20px; text-align: center; font-family: "Montserrat", sans-serif; font-weight: 800; font-size: 36px; color: var(--white); letter-spacing: 0.5px; }

  /* Back */
  .tag-back { left: 640px; top: 513px; background: var(--white); }
  .tag-back .edge-band { background: linear-gradient(180deg, var(--blue-light), var(--blue)); }
  .tag-back .edge-left { left: 0; }
  .tag-back .edge-right { right: 0; top: 150px; }

  .corner-badge { position: absolute; right: 0; top: 0; width: 136px; height: 148px; background: var(--blue); border-bottom-left-radius: 44px; }
  .mini-digit { position: absolute; font-family: "Poppins", sans-serif; font-weight: 600; font-size: 62px; line-height: 1; color: var(--white); }
  .mini-2a { left: 14px; top: 22px; }
  .mini-2b { left: 30px; top: 74px; }
  .mini-6 { left: 66px; top: 74px; color: var(--pink); }
  .mini-ring { position: absolute; left: 52px; top: 29px; width: 50px; height: 50px; border-radius: 50%; border: 8px solid var(--white); }

  .back-title { position: absolute; left: 56px; top: 122px; font-family: "Montserrat", sans-serif; font-weight: 800; font-size: 36px; line-height: 38px; color: var(--blue); }
  .back-title .accent { color: var(--pink); }

  .title-rule { position: absolute; left: 40px; right: 30px; top: 282px; height: 3px; background: linear-gradient(90deg, transparent, var(--blue) 20%, var(--blue) 80%, transparent); }

  .field { position: absolute; left: 48px; font-family: "Montserrat", sans-serif; }
  .field-label { font-weight: 800; font-size: 27px; line-height: 30px; color: var(--blue); }
  .field-value { font-weight: 400; font-size: 33px; line-height: 34px; color: var(--pink); }
  .field-name { top: 295px; }
  .field-age { top: 375px; }
  .field-events { top: 455px; }

  .back-hashtag { position: absolute; left: 75px; bottom: 0; width: 260px; height: 60px; border-radius: 30px 30px 0 0; background: var(--blue); display: flex; align-items: center; justify-content: center; font-family: "Montserrat", sans-serif; font-weight: 800; font-size: 28px; color: var(--pink); }
</style>
</head>
<body>
<main class="canvas">

  <section class="tag tag-front" aria-label="Bag tag front">
    <div class="edge-band edge-left" role="img" aria-label="Wave pattern border"></div>
    <div class="edge-band edge-right" role="img" aria-label="Wave pattern border"></div>
    <div class="tag-slot"></div>
    <span class="year-digit year-2a">2</span>
    <div class="year-ring"><span class="ring-name">MAPLE<br>HOLLOW</span></div>
    <span class="year-digit year-2b">2</span>
    <span class="year-digit year-6">6</span>
    <p class="front-hashtag">#PADDLESOUT</p>
  </section>

  <section class="tag tag-back" aria-label="Bag tag back">
    <div class="edge-band edge-left" role="img" aria-label="Wave pattern border"></div>
    <div class="edge-band edge-right" role="img" aria-label="Wave pattern border"></div>
    <div class="tag-slot"></div>
    <div class="corner-badge">
      <span class="mini-digit mini-2a">2</span>
      <div class="mini-ring"></div>
      <span class="mini-digit mini-2b">2</span>
      <span class="mini-digit mini-6">6</span>
    </div>
    <h1 class="back-title">MAPLE<br>HOLLOW<br>OTTERS<br><span class="accent">SWIM 2026</span></h1>
    <div class="title-rule"></div>
    <div class="field field-name"><p class="field-label">ATHLETE NAME:</p><p class="field-value">LOREM IPSUM</p></div>
    <div class="field field-age"><p class="field-label">AGE GROUP:</p><p class="field-value">9-10</p></div>
    <div class="field field-events"><p class="field-label">EVENTS:</p><p class="field-value">LOREM IPSUM</p></div>
    <p class="back-hashtag">#PADDLESOUT</p>
  </section>

</main>
</body>
</html>
```